Business Card Design

We currently have a business card design for our main business 'Lantern Walls"
We are reasonably happy with our current design for Lantern Walls business card (black damask patterned wallpaper in background white simplistic font with white chandelier (see logo on website). www.lanternwalls.com.au

We are considering whether its in our best interest to have a separate business card OR a double sided card to promote our secondary business 'Glow Cones'. We are open to either a double-sided card with one business on each side OR a double sided card for each business. With contact info on the back of each.

We need a new snazzy design for 'Glow Cones' our custom made lampshades from which we craft from our wallpaper designs. We had an idea that we could use the top swatch shown on this link below as the pattern in the background (Orange/black) geometric triangles.
http://www.lanternwalls.com.au/product_info.php?products_id=1086

For the glow cones Font we would be happy with something similar to Lantern Walls but perhaps a little more handmade/arty slant.
Below another link shows you a few of our lampshades
http://www.lanternwalls.com.au/index.php?cPath=10

For Glow Cones I think we also need the quote under in smaller font
"Custom-Made Wallpaper Lampshades"

Target Market(s)

Glow Cones will be for the Young Funky Apartment Dwellers, Young Families Styling Home Decor and Kids Rooms. It also attracts small business owners doing shop-fits.

Industry/Entity Type

Business

Contact Information for Business Card

We need to incorporate our sister business to the back side of our business card. I am also open to having two different business cards if designers think this will not be possible.
We need the same contact info, different logo.
ABN: 47 302 916 584
Email: sales@lanternwalls.com.au
Postal Address: PO Box 731, Kelvale VIC 3294
Website: http://www.lanternwalls.com.au

Requirements
Must have
• A hand-made arty appeal for Glow Cones
Was unable to get sliders to work for the look and feel so below is the best list from the above:
Bold, Playful, Modern, Personable, Colorful, Upmarket.
Nice to have
• We love the bold contrasting colors. Colors chosen for our website were Orange, Blue and Duck Egg Bright Blue!

```html
<!DOCTYPE html>
<html lang="en">
<head>
<meta charset="utf-8">
<title>Lantern Walls &amp; Glow Cones Business Cards</title>
<link rel="stylesheet" href="https://fonts.googleapis.com/css2?family=Questrial&family=Poiret+One&display=swap">
<style>
  :root {
    --page: #ffffff;
    --card-dark: #0a0a0a;
    --card-light: #ffffff;
    --ink-light: #ffffff;
    --ink-dark: #111111;
    --ink-logo: #3a3a3a;
    --accent-orange: #f15a24;
    --accent-mint: #a8efde;
    --damask-deep: #1c1c1c;
    --damask-mid: #4a4a4a;
    --shadow: rgba(0, 0, 0, 0.55);
  }
  * { margin: 0; padding: 0; box-sizing: border-box; }
  html, body {
    width: 1200px;
    height: 999px;
    overflow: hidden;
    background: var(--page);
  }
  .canvas {
    position: relative;
    width: 1200px;
    height: 999px;
    font-family: "Questrial", "Century Gothic", sans-serif;
  }
  .card {
    position: absolute;
    box-shadow: -14px 12px 8px var(--shadow);
  }

  /* Front: Lantern Walls */
  .card--front {
    left: 332px;
    top: 159px;
    width: 537px;
    height: 332px;
    background: var(--card-dark);
  }
  .front-banner {
    position: absolute;
    left: 20px;
    top: 21px;
    width: 488px;
    height: 100px;
    background: linear-gradient(90deg, var(--damask-mid) 0%, var(--damask-deep) 45%, var(--damask-mid) 75%, var(--damask-deep) 100%);
  }
  .front-brand {
    position: absolute;
    left: 30px;
    top: 41px;
    font-size: 31px;
    color: var(--ink-light);
    letter-spacing: -0.5px;
  }
  .front-rule {
    position: absolute;
    left: 0;
    top: 122px;
    width: 100%;
    height: 3px;
    background: var(--ink-light);
  }
  .front-contact {
    position: absolute;
    left: 0;
    top: 226px;
    width: 100%;
    text-align: center;
    color: var(--ink-light);
    font-size: 16.5px;
    line-height: 22px;
    list-style: none;
  }

  /* Back: Glow Cones */
  .card--back {
    left: 332px;
    top: 549px;
    width: 526px;
    height: 321px;
    background: var(--card-light);
  }
  .back-pattern {
    position: absolute;
    left: 20px;
    top: 9px;
    width: 140px;
    height: 293px;
    background: linear-gradient(160deg, var(--accent-orange) 0%, var(--accent-mint) 35%, var(--ink-dark) 60%, var(--accent-orange) 82%, var(--accent-mint) 100%);
  }
  .back-brand {
    position: absolute;
    right: 8px;
    top: 8px;
    font-family: "Poiret One", "Questrial", sans-serif;
    font-size: 42px;
    color: var(--ink-logo);
    letter-spacing: 2px;
  }
  .back-tagline {
    position: absolute;
    left: 232px;
    top: 57px;
    width: 276px;
    text-align: center;
    font-size: 14px;
    color: var(--accent-mint);
  }
  .back-contact {
    position: absolute;
    right: 9px;
    top: 227px;
    text-align: right;
    list-style: none;
    font-size: 15px;
    line-height: 19.7px;
    color: var(--ink-dark);
  }
  .back-contact .label { color: var(--accent-orange); }
</style>
</head>
<body>
<main class="canvas">

  <section class="card card--front" aria-label="Lantern Walls card">
    <div class="front-banner" role="img" aria-label="Black damask wallpaper band with white chandeliers"></div>
    <div class="front-brand">Lantern Walls</div>
    <div class="front-rule"></div>
    <ul class="front-contact">
      <li>ABN: 47 302 916 584</li>
      <li>Email: sales@lanternwalls.com.au</li>
      <li>Postal Address: PO Box 731, Kelvale VIC 3294</li>
      <li>Website: http://www.lanternwalls.com.au</li>
    </ul>
  </section>

  <section class="card card--back" aria-label="Glow Cones card">
    <div class="back-pattern" role="img" aria-label="Geometric triangle pattern in orange, duck egg blue and black"></div>
    <div class="back-brand">Glow Cones</div>
    <div class="back-tagline">Custom-Made Wallpaper Lampshades</div>
    <ul class="back-contact">
      <li><span class="label">ABN:</span> 47 302 916 584</li>
      <li><span class="label">Email:</span> sales@lanternwalls.com.au</li>
      <li><span class="label">Postal Address:</span> PO Box 731, Kelvale VIC 3294</li>
      <li><span class="label">Website:</span> http://www.lanternwalls.com.au</li>
    </ul>
  </section>

</main>
</body>
</html>
```